Bakery Replacement Lighted Sign Face

We are opening a new bakery that sells only cakes. The name is "The Willow Lantern." We are replacing the current sign face with a new look that states our name and makes a bold statement of fun. We will be known for having 101 cakes that are always ready for immediate pickup or delivery. Our colors are pink, orange, and lime green. An image is provided to see the colors.

Target Market(s)

people who buy cakes for parties and all other occasions

Industry/Entity Type

Cakes

Other font styles liked:
• look at the logo and file for the main font name

Colors
59FF00
82FF00
B8FF75
E3FFCB
F4FFEA
F0912C
F2A743
F7CA91
FBE8D2
FDF5EE
EB3D1F
EC4F4E
F09395
F8D3D4
FCEDEE

Requirements
Must have
• The name of the bakery. Logo can be used as is or changed as shown in one of the uploaded PDFs. Must use either pink, orange, lime green, white, or black. We prefer a bright pink background with white lettering as our first choice, but are willing to be open minded to see all creative concepts. Also the sign is 14 feet long and 42 inches tall so the artwork must fit within those boundaries. Also keep in mind the sign does have a 4 inch black frame. So the graphics area is actually 13 feet 2 inches by 3 feet. Also, in the attached pdf that shows a rough possible layout, the words "101 cakes to go" is on the sign. It is NOT a must. Only use the wording if it adds to your design.
Nice to have
• You are welcome to add additional stars or other fun graphics that could look good.
Should not have
• No images of cakes or other bakery products.

```html
<!DOCTYPE html>
<html lang="en">
<head>
<meta charset="utf-8">
<title>The Willow Lantern – Sign Face</title>
<link href="https://fonts.googleapis.com/css2?family=Fredoka:wght@500;600;700&display=swap" rel="stylesheet">
<style>
  :root {
    --backdrop: #a3a3a3;
    --white: #ffffff;
    --pink-deep: #ff1479;
    --pink-light: #ff72b4;
    --coral: #f27c72;
    --purple: #4b1f6e;
    --lime: #e3ff55;
  }
  * { box-sizing: border-box; margin: 0; padding: 0; }
  html, body { width: 1200px; height: 536px; overflow: hidden; background: var(--backdrop); }
  .sign {
    position: absolute; left: 0; top: 118px;
    width: 1200px; height: 300px;
    background: var(--white);
    overflow: hidden;
  }
  .sign__field { position: absolute; inset: 0; width: 1200px; height: 300px; }
  .brand {
    position: absolute; left: 146px; top: 56px; width: 280px;
    font-family: "Fredoka", sans-serif; font-weight: 600;
    color: var(--coral); font-size: 54px; line-height: 1.02;
    text-align: center;
  }
  .headline {
    position: absolute; left: 581px; top: 34px;
    display: flex; align-items: center; gap: 12px;
  }
  .headline__title {
    font-family: "Fredoka", sans-serif; font-weight: 600;
    font-size: 116px; line-height: 1; letter-spacing: 3px;
    color: var(--white);
    -webkit-text-stroke: 16px var(--purple);
    paint-order: stroke fill;
  }
  .headline__badge {
    width: 52px; height: 78px; border-radius: 10px;
    background: var(--lime); color: var(--purple);
    font-family: "Fredoka", sans-serif; font-weight: 600;
    font-size: 25px; line-height: 1.05;
    display: flex; flex-direction: column; align-items: center; justify-content: center;
  }
  .tagline {
    position: absolute; left: 570px; width: 576px; top: 148px;
    font-family: "Fredoka", sans-serif; font-weight: 600;
    font-size: 22px; line-height: 29px; text-align: center;
    color: var(--white);
  }
  .tagline__accent { color: var(--lime); display: block; }
  .web-link {
    position: absolute; left: 670px; top: 220px; width: 377px; height: 35px;
    border-radius: 18px; background: var(--lime); border: 1.5px solid var(--purple);
    font-family: "Fredoka", sans-serif; font-weight: 600; font-size: 19px;
    color: var(--purple); letter-spacing: 1.5px;
    display: flex; align-items: center; justify-content: center;
  }
</style>
</head>
<body>
  <main class="sign">
    <svg class="sign__field" viewBox="0 0 1200 300" role="img" aria-label="Bright pink paint splash sweeping across the sign">
      <defs>
        <radialGradient id="pinkGlow" cx="0.6" cy="0.55" r="0.6">
          <stop offset="0" stop-color="#ff72b4"/>
          <stop offset="1" stop-color="#ff1479"/>
        </radialGradient>
      </defs>
      <path fill="url(#pinkGlow)"
        d="M581 0 H1200 V300 H108
           C180 260 260 250 330 232
           C420 210 480 190 520 140
           C550 100 560 40 581 0 Z"/>
      <g fill="#e3ff55">
        <path d="M978 8 l4 9 10 1 -7 7 2 10 -9 -5 -9 5 2 -10 -7 -7 10 -1 z"/>
        <path d="M537 190 l8 17 19 3 -14 13 4 19 -17 -9 -17 9 4 -19 -14 -13 19 -3 z"/>
        <path d="M1104 243 l4 8 9 1 -6 6 1 9 -8 -4 -8 4 1 -9 -6 -6 9 -1 z"/>
      </g>
    </svg>

    <div class="brand">The Willow<br>Lantern</div>

    <div class="headline">
      <h1 class="headline__title">101 cakes</h1>
      <div class="headline__badge"><span>TO</span><span>GO</span></div>
    </div>

    <p class="tagline">
      101 cakes that are always ready for immediate
      <span class="tagline__accent">pickup or delivery</span>
    </p>

    <div class="web-link">www.willowlanterncakes.com</div>
  </main>
</body>
</html>
```